Willowbrook Body Care business is seeking a Business Card Design

We are a new natural therapy business that needs a Business Card Design with an appointment card on the back.

We offer Myotherapy (muscle therapy) services and have a strong focus and commitment to helping people relieve pain and restore movement to their bodies.

I am attaching my business logo for you information.

Business card must contain my logo and have space for name, title, qualifications, phone number, email, web address

Appointment Card on the back of the card must contain space to write next appointment date, time and name of therapist and cancellation policy.

Cancellation Policy
Minimum of 24hrs notice is required prior to appointment time or full treatment fees with apply.

Industry/Entity Type

Business

```html
<!DOCTYPE html>
<html lang="en">
<head>
<meta charset="utf-8">
<title>Willowbrook Body Care – Business Card</title>
<link rel="stylesheet" href="https://fonts.googleapis.com/css2?family=Quicksand:wght@400;500;700&display=swap">
<style>
  :root {
    --brand-red: #c0001f;
    --brand-green: #77f200;
    --paper: #ffffff;
  }
  html, body {
    margin: 0;
    padding: 0;
    width: 1200px;
    height: 741px;
    overflow: hidden;
    background: var(--paper);
  }
  .card {
    position: relative;
    width: 1200px;
    height: 741px;
    background: var(--paper);
    font-family: "Quicksand", sans-serif;
    overflow: hidden;
  }
  .card__panel {
    position: absolute;
    inset: 0;
  }
  .brand {
    position: absolute;
    left: 30px;
    width: 492px;
    top: 300px;
    text-align: center;
  }
  .brand__mark {
    width: 90px;
    height: 90px;
    background: var(--brand-red);
    margin: 0 auto 26px;
  }
  .brand__name {
    margin: 0;
    color: var(--brand-red);
    font-weight: 700;
    font-size: 37px;
    letter-spacing: 0.5px;
    line-height: 1.1;
  }
  .person {
    position: absolute;
    left: 640px;
    width: 468px;
    top: 72px;
    text-align: center;
    color: var(--paper);
    font-weight: 700;
  }
  .person__name {
    margin: 0;
    color: var(--brand-red);
    font-size: 42px;
    letter-spacing: 1px;
    line-height: 1.1;
  }
  .person__title {
    margin: 4px 0 0 22px;
    font-size: 33px;
    line-height: 1.15;
  }
  .person__qualification {
    margin: 6px 0 0 22px;
    font-size: 26px;
  }
  .contact {
    position: absolute;
    left: 551px;
    display: flex;
    align-items: center;
    gap: 30px;
    color: var(--paper);
    font-weight: 400;
    font-size: 28px;
    letter-spacing: 0.5px;
    line-height: 1.45;
  }
  .contact__icon {
    width: 81px;
    height: 81px;
    flex: none;
    display: block;
  }
  .contact--phone { top: 216px; }
  .contact--email { top: 326px; }
  .contact--web { top: 440px; }
  .contact--address { top: 551px; align-items: flex-start; }
  .contact--address .contact__text { margin-top: 26px; }
</style>
</head>
<body>
<div class="card">
  <svg class="card__panel" width="1200" height="741" viewBox="0 0 1200 741" aria-hidden="true">
    <path d="M508 0 C 520 120, 560 220, 585 360 C 605 480, 545 600, 525 741 L 1200 741 L 1200 0 Z" fill="var(--brand-green)"/>
    <path d="M508 0 C 520 120, 560 220, 585 360 C 605 480, 545 600, 525 741" fill="none" stroke="var(--brand-red)" stroke-width="11"/>
  </svg>

  <div class="brand">
    <div class="brand__mark"></div>
    <p class="brand__name">Willowbrook Body Care</p>
  </div>

  <div class="person">
    <h1 class="person__name">Clara Benton</h1>
    <p class="person__title">Myotherapist</p>
    <p class="person__qualification">Adv. Dip. Myotherapy</p>
  </div>

  <div class="contact contact--phone">
    <svg class="contact__icon" viewBox="0 0 81 81" aria-hidden="true">
      <rect x="3" y="3" width="75" height="75" rx="4" fill="#fff" stroke="var(--brand-red)" stroke-width="5"/>
      <path d="M16 32 C 16 20, 65 20, 65 32 L 65 36 L 54 36 L 54 31 L 27 31 L 27 36 L 16 36 Z" fill="var(--brand-red)"/>
      <path d="M24 40 L 57 40 L 62 60 L 19 60 Z" fill="var(--brand-red)"/>
      <g fill="#fff">
        <rect x="33" y="44" width="4" height="3"/><rect x="39" y="44" width="4" height="3"/><rect x="45" y="44" width="4" height="3"/>
        <rect x="33" y="49" width="4" height="3"/><rect x="39" y="49" width="4" height="3"/><rect x="45" y="49" width="4" height="3"/>
        <rect x="33" y="54" width="4" height="3"/><rect x="39" y="54" width="4" height="3"/><rect x="45" y="54" width="4" height="3"/>
      </g>
    </svg>
    <span class="contact__text">+61 3 9012 4567</span>
  </div>

  <div class="contact contact--email">
    <svg class="contact__icon" viewBox="0 0 81 81" aria-hidden="true">
      <rect x="3" y="3" width="75" height="75" rx="4" fill="#fff" stroke="var(--brand-red)" stroke-width="5"/>
      <rect x="15" y="22" width="51" height="37" fill="var(--brand-red)"/>
      <path d="M17 24 L 40.5 44 L 64 24 M17 57 L 34 39 M64 57 L 47 39" fill="none" stroke="#fff" stroke-width="2"/>
    </svg>
    <span class="contact__text">info@willowbrookbodycare.com.au</span>
  </div>

  <div class="contact contact--web">
    <svg class="contact__icon" viewBox="0 0 81 81" aria-hidden="true">
      <rect x="3" y="3" width="75" height="75" rx="4" fill="#fff" stroke="var(--brand-red)" stroke-width="5"/>
      <circle cx="40.5" cy="40.5" r="25" fill="var(--brand-red)"/>
      <circle cx="40.5" cy="40.5" r="19" fill="#fff"/>
      <path d="M30 28 C 36 26, 42 30, 40 36 C 38 42, 30 40, 28 46 C 26 40, 25 33, 30 28 Z M44 44 C 50 42, 56 46, 52 54 C 48 58, 44 52, 44 44 Z" fill="var(--brand-red)"/>
    </svg>
    <span class="contact__text">www.willowbrookbodycare.com.au</span>
  </div>

  <div class="contact contact--address">
    <svg class="contact__icon" viewBox="0 0 81 81" aria-hidden="true">
      <rect x="3" y="3" width="75" height="75" rx="4" fill="#fff" stroke="var(--brand-red)" stroke-width="5"/>
      <path d="M13 42 L 40.5 17 L 68 42 L 62 42 L 40.5 23 L 19 42 Z" fill="var(--brand-red)"/>
      <path d="M21 42 L 40.5 25 L 60 42 L 60 63 L 46 63 L 46 49 L 35 49 L 35 63 L 21 63 Z" fill="var(--brand-red)"/>
    </svg>
    <span class="contact__text">Level 1/58 Elmstone Rd,<br>Ashgrove VIC 3095</span>
  </div>
</div>
</body>
</html>
```